Harbour Wing Flights business card

I need a business card designed based on our logo -- designed by Studio Flock designers.

The logo is to be taken from our web site at www.harbourwingflights.com.au

I need to have this card designed quickly as its needed for business meetings
Updates

Hi Designers, Please see my updated brief for my business card. I have attached logo images and a brochure for inspiration... Regards, Gavin Trelford Harbour Wing Flights

Target Market(s)

Hotel owners and operators (concierge) and tourists to Australia

Industry/Entity Type

Business

Font styles to use
Sans Serif

Colors
84abd2
3176b5
85abd2
cedeec

Requirements
Must have
• Utilise our logo. Found on our web page www.harbourwingflights.com.au

SIDE 1
Must have my name: Gavin Trelford
Title:Owner
Phone number: 1300 418 396
Mobile:0461273958

SIDE 2
LOGO
PREPARE TO BE AMAZED! (see attached brochure for information and font style)
Nice to have
• Something that reflects aviation and tour with a light aircraft

```html
<!DOCTYPE html>
<html lang="en">
<head>
<meta charset="utf-8">
<title>Harbour Wing Flights – Business Card</title>
<link rel="stylesheet" href="https://fonts.googleapis.com/css2?family=Open+Sans:wght@400;600;700&display=swap">
<style>
  :root {
    --backdrop: #c9ced4;
    --card-white: #ffffff;
    --card-shade: #eceef0;
    --panel-grey: #414141;
    --accent-blue: #0000a0;
    --logo-grey: #555a60;
    --text-light: #ffffff;
  }
  * { margin: 0; padding: 0; box-sizing: border-box; }
  html, body {
    width: 1200px;
    height: 865px;
    overflow: hidden;
    background: var(--backdrop);
    font-family: "Open Sans", Arial, sans-serif;
  }
  .business-card {
    position: absolute;
    left: 100px;
    top: 146px;
    width: 1000px;
    height: 572px;
    background: radial-gradient(circle at 30% 45%, var(--card-white) 0%, var(--card-shade) 100%);
    overflow: hidden;
    box-shadow: 0 10px 30px rgba(0,0,0,0.18);
  }
  .card-shapes {
    position: absolute;
    inset: 0;
    width: 100%;
    height: 100%;
  }
  .brand-lockup {
    position: absolute;
    left: 150px;
    top: 282px;
    display: flex;
    align-items: center;
    gap: 12px;
    color: var(--logo-grey);
    font-weight: 600;
    font-size: 22px;
    letter-spacing: 1px;
    text-transform: uppercase;
  }
  .brand-dot {
    width: 18px;
    height: 18px;
    border-radius: 50%;
    background: var(--accent-blue);
  }
  .contact-block {
    position: absolute;
    right: 70px;
    top: 70px;
    text-align: right;
    color: var(--text-light);
    font-size: 22px;
    line-height: 1.4;
  }
  .person-name { font-weight: 700; font-size: 26px; line-height: 1.25; }
  .person-title { font-size: 24px; margin-bottom: 58px; }
  .address { margin-bottom: 14px; }
  .contact-line { display: flex; justify-content: flex-end; align-items: center; gap: 8px; }
  .contact-icon { width: 18px; height: 18px; fill: var(--text-light); }
  .web-line { margin-top: 10px; }
</style>
</head>
<body>
  <div class="business-card">
    <svg class="card-shapes" viewBox="0 0 1000 572" aria-hidden="true">
      <path class="accent-crescent" fill="var(--accent-blue)"
            d="M520,120 C610,260 560,460 420,572 L720,572 L720,120 Z"/>
      <path class="info-panel" fill="var(--panel-grey)" stroke="var(--card-white)" stroke-width="14"
            d="M330,-10 C560,90 680,300 588,582 L1010,582 L1010,-10 Z"/>
    </svg>

    <div class="brand-lockup">
      <span class="brand-dot"></span>
      <span class="brand-name">Harbour Wing Flights</span>
    </div>

    <div class="contact-block">
      <p class="person-name">Corin Halvey-Marsh</p>
      <p class="person-title">Consultant</p>
      <p class="address">047 12th floor,Quay<br>Harbour Lane NSW</p>
      <p class="contact-line">012 555 0147
        <svg class="contact-icon" viewBox="0 0 24 24"><path d="M6.6 10.8a15 15 0 0 0 6.6 6.6l2.2-2.2a1 1 0 0 1 1-.25 11.4 11.4 0 0 0 3.6.57 1 1 0 0 1 1 1V20a1 1 0 0 1-1 1A17 17 0 0 1 3 4a1 1 0 0 1 1-1h3.5a1 1 0 0 1 1 1c0 1.25.2 2.45.57 3.57a1 1 0 0 1-.25 1z"/></svg>
      </p>
      <p class="contact-line">012 555 0147
        <svg class="contact-icon" viewBox="0 0 24 24"><path d="M7 2h8v6H7zM4 9h16v13H4zm3 3v2h2v-2zm4 0v2h2v-2zm4 0v2h2v-2zm-8 4v2h2v-2zm4 0v2h2v-2zm4 0v2h2v-2z"/></svg>
      </p>
      <p class="contact-line">name@mailbox.com
        <svg class="contact-icon" viewBox="0 0 24 24"><path d="M2 5h20v14H2zm2 2v.5l8 5.5 8-5.5V7l-8 5.5z"/></svg>
      </p>
      <p class="web-line">www.yourcompanysite.com</p>
    </div>
  </div>
</body>
</html>
```